Quarn Corporate Letterhead

- We would like a letterhead using our logo (can be supplied as vector if needed)
- Would like to have the logo on a clear background
- Please send logo design as a separate file
- Letterhead information:
Quarn Energy Inc.
482 W. Brook Ave. Suite 214
Pasadena, CA 91847

Colors
0555a3
3276b5
85abd2
000000
1b1b1b
757575
c7c7c7
e8e8e8

```html
<!DOCTYPE html>
<html lang="en">
<head>
<meta charset="utf-8">
<title>Quarn Corporate Letterhead</title>
<link rel="stylesheet" href="https://fonts.googleapis.com/css2?family=Open+Sans:wght@400;600;700&display=swap">
<style>
  :root {
    --brand-blue: #0555a3;
    --brand-mid: #3276b5;
    --brand-light: #85abd2;
    --navy: #0b2a6b;
    --ink: #1b1b1b;
    --muted: #757575;
    --silver: #c7c7c7;
    --backdrop: #e8e8e8;
    --paper: #ffffff;
  }
  * { box-sizing: border-box; margin: 0; padding: 0; }
  html, body {
    width: 1200px;
    height: 795px;
    overflow: hidden;
  }
  body {
    background: var(--backdrop);
    font-family: "Open Sans", sans-serif;
    color: var(--ink);
  }
  .letterhead {
    position: absolute;
    left: 340px;
    top: 30px;
    width: 520px;
    height: 735px;
    background: var(--paper);
    box-shadow: 0 2px 10px rgba(0,0,0,0.12);
  }
  .edge-band {
    position: absolute;
    left: 0;
    width: 14px;
  }
  .edge-band--silver {
    top: 0;
    height: 92px;
    background: linear-gradient(180deg, #9a9a9a 0%, #e4e4e4 35%, #8c8c8c 70%, #d2d2d2 100%);
  }
  .edge-band--blue {
    top: 96px;
    bottom: 0;
    background: linear-gradient(180deg, var(--navy) 0%, var(--brand-blue) 40%, var(--brand-mid) 62%, var(--brand-blue) 82%, var(--navy) 100%);
  }
  .brand-name {
    position: absolute;
    left: 44px;
    top: 44px;
    font-size: 30px;
    font-weight: 700;
    color: var(--brand-blue);
    letter-spacing: -0.5px;
    line-height: 1;
  }
  .sender-address {
    position: absolute;
    right: 48px;
    top: 46px;
    font-size: 8.5px;
    line-height: 1.3;
    color: var(--muted);
  }
  .sender-address .company {
    font-weight: 700;
    color: var(--brand-blue);
  }
  .letter-body {
    position: absolute;
    left: 64px;
    right: 48px;
    top: 150px;
    font-size: 7.6px;
    line-height: 1.55;
    color: var(--muted);
  }
  .salutation {
    font-size: 12px;
    color: var(--ink);
    margin-bottom: 12px;
  }
  .letter-body p + p { margin-top: 11px; }
  .closing {
    position: absolute;
    left: 64px;
    top: 480px;
    font-size: 7.6px;
    color: var(--muted);
  }
  .signature-mark {
    display: block;
    margin: 8px 0 4px 30px;
  }
  .signer {
    margin-left: 30px;
    font-size: 8px;
    line-height: 1.4;
    color: var(--muted);
  }
</style>
</head>
<body>
  <main class="letterhead">
    <div class="edge-band edge-band--silver"></div>
    <div class="edge-band edge-band--blue"></div>

    <div class="brand-name">Quarn</div>

    <address class="sender-address">
      <div class="company">Quarn Energy Inc.</div>
      <div>482 W. Brook Ave. Suite 214</div>
      <div>Pasadena, CA 91847</div>
    </address>

    <section class="letter-body">
      <div class="salutation">Dear Mr. Carter,</div>
      <p>Lorem ipsum dolor sit amet, consectetur adipiscing elit. Donec orci purus, luctus vitae dignissim eu, iaculis sed purus. Vivamus faucibus, ipsum nec aliquet viverra, leo mauris condimentum ligula, sit amet sagittis enim ligula quis arcu. Nam egestas tortor id nisl porttitor mattis. In tortor ante, ultricies in suscipit a, tempus non massa. Vivamus et auctor mi. Fusce vel massa nulla. Phasellus nec eros mauris, et scelerisque orci.</p>
      <p>Donec malesuada orci vitae nulla accumsan porta a id massa. Quisque accumsan iaculis magna sit amet fringilla. Maecenas consequat, magna eget tincidunt semper, odio nibh rutrum mi, id feugiat ante nisi eu risus. Vestibulum nunc orci, rhoncus a placerat in, ultricies in mi. Cras mattis varius eros, vel fringilla nisi suscipit eget. Quisque scelerisque sagittis nulla at porttitor.</p>
      <p>Sed id augue vitae urna euismod commodo aliquet a quam. Pellentesque arcu velit, cursus et malesuada ut, consequat et diam. Nullam erat sem, rhoncus id ullamcorper vitae, rhoncus at arcu. In ultricies ultricies nulla, ut rutrum nisl iaculis at. Donec eu magna a metus ornare faucibus. Fusce aliquet faucibus ultricies. Morbi semper, est id tincidunt gravida, sem arcu adipiscing lacus, ac bibendum nulla leo eu purus. Quisque nec diam sed risus consectetur accumsan quis quis nibh. Vestibulum id purus lorem.</p>
      <p>It is a long established fact that a reader will be distracted by the readable content of a page when looking at its layout. The point of using Lorem Ipsum is that it has a more-or-less normal distribution of letters, as opposed to using 'Content here, content here', making it look like readable English. Many desktop publishing packages.</p>
    </section>

    <div class="closing">
      <div>Sincerely,</div>
      <svg class="signature-mark" width="70" height="26" role="img" aria-label="Handwritten signature of the sender">
        <rect width="70" height="26" rx="3" fill="#e8e8e8"/>
      </svg>
      <div class="signer">Evan Hale<br>CEO/ Founder</div>
    </div>
  </main>
</body>
</html>
```